Ora- luxurious rental suites coming soon

Looking for a large size banner design. The banner will include the logo "ORA". The logo has already been designed by one of your designers (Belmiro). The banner is to be placed on the building fence and will be used as a marketing/ advertisement purpose to display what's coming soon. It needs to be clean and elegant since it's representing upscale apartements.
Requesting Belmiro to be one of the designers. Thanks.
Updates

Hi all-here is the logo link. Banner will be printed on 3 separate boards that will be attached side by side to look like one big one. We are doing it this way to be able to make future modifications on 1 board at a time. Each board will be 10'Wx8'H panel. Logo design needs to be in the middle board and other left and right side boards will have the info like "coming soon and building picture". For now, please use any building image, I will be sending the actual building image later on for an update. Please do not include full image of building, choose a section and zoom or crop portion of building image so it looks more interesting. Building will be a luxurious rental in downtown. Thanks. https://www.filecrate.net/sh/k4mwpxq7r2d9vzb/QRT8LMN2K_hx_WBZcpfkeH3Lo?dl=0x

Re: banner: Instead of "coming soon" please use "coming this fall'. Thanks

Target Market(s)

professionals

Industry/Entity Type

Residential rentals

Font styles to use
Serif

Requirements
Must have
• use wording such as: coming this fall, 1&2 bedroom suites, designer finishes, terrace views
Nice to have
• Banner will be placed on site over a black mesh backdrop. Please design in a way that will make it look like blending with mesh
Should not have
• Banner should not be too colorf. Please use white, grey or yellow... refer to logo image

```html
<!DOCTYPE html>
<html lang="en">
<head>
<meta charset="UTF-8">
<title>ORA – Coming This Fall</title>
<link href="https://fonts.googleapis.com/css2?family=Oswald:wght@300;700&display=swap" rel="stylesheet">
<style>
  :root {
    --black: #000000;
    --yellow: #ffc800;
    --white: #ffffff;
    --name-grey: #7f8c84;
    --address-grey: #8a8f8c;
  }
  html, body {
    margin: 0;
    padding: 0;
    width: 1200px;
    height: 320px;
    overflow: hidden;
    background: var(--black);
  }
  .banner {
    position: relative;
    width: 1200px;
    height: 320px;
    overflow: hidden;
    background: var(--black);
  }
  .interior-photo {
    position: absolute;
    left: 0;
    top: 0;
    width: 800px;
    height: 320px;
    background:
      linear-gradient(90deg, rgba(0,0,0,0.55) 0%, rgba(0,0,0,0.15) 35%, rgba(0,0,0,0.55) 62%, #000 88%),
      linear-gradient(180deg, #1c2127 0%, #2b2c2e 35%, #3a3a38 60%, #1d1d1d 100%);
  }
  .taglines {
    position: absolute;
    right: calc(1200px - 368px);
    top: 103px;
    text-align: right;
    font-family: "Oswald", sans-serif;
    text-transform: uppercase;
  }
  .tagline-lead {
    margin: 0;
    font-weight: 700;
    font-size: 34px;
    line-height: 40px;
    letter-spacing: 3px;
    color: var(--yellow);
  }
  .tagline-item {
    margin: 0;
    font-weight: 300;
    font-size: 34px;
    line-height: 37px;
    letter-spacing: 2px;
    color: var(--white);
  }
  .divider {
    position: absolute;
    left: 384px;
    top: 110px;
    width: 3px;
    height: 106px;
    background: var(--yellow);
  }
  .address {
    position: absolute;
    left: 557px;
    top: 74px;
    margin: 0;
    font-family: "Oswald", sans-serif;
    font-weight: 300;
    font-size: 20px;
    line-height: 26px;
    letter-spacing: 8px;
    color: var(--address-grey);
  }
  .brand-name {
    position: absolute;
    left: 424px;
    top: 93px;
    margin: 0;
    font-family: "Oswald", sans-serif;
    font-weight: 300;
    font-size: 150px;
    line-height: 150px;
    letter-spacing: 24px;
    color: var(--name-grey);
  }
  .building-panel {
    position: absolute;
    right: 0;
    top: 0;
    width: 420px;
    height: 320px;
  }
</style>
</head>
<body>
  <main class="banner">
    <div class="interior-photo" role="img" aria-label="Dim photo of a modern apartment living room with floor-to-ceiling windows overlooking a city skyline"></div>

    <div class="taglines">
      <p class="tagline-lead">Coming This Fall</p>
      <p class="tagline-item">1&amp;2 Bedroom Suites</p>
      <p class="tagline-item">Designer Finishes</p>
    </div>

    <div class="divider"></div>

    <p class="address">415 HALDEN</p>
    <h1 class="brand-name">ORA</h1>

    <svg class="building-panel" viewBox="0 0 420 320" xmlns="http://www.w3.org/2000/svg">
      <defs>
        <linearGradient id="courtyard-tones" x1="0" y1="0" x2="0" y2="1">
          <stop offset="0" stop-color="#3b3a3c"/>
          <stop offset="0.35" stop-color="#5a4c42"/>
          <stop offset="0.6" stop-color="#6e5a48"/>
          <stop offset="0.8" stop-color="#4f6f78"/>
          <stop offset="1" stop-color="#3a3230"/>
        </linearGradient>
      </defs>
      <path d="M19 0 C 55 40, 76 90, 72 140 C 68 175, 44 190, 44 215 C 44 260, 70 295, 92 320 L 420 320 L 420 0 Z" fill="var(--yellow)"/>
      <path d="M30 0 C 66 40, 86 90, 82 140 C 78 175, 54 190, 54 215 C 54 258, 80 295, 104 320 L 420 320 L 420 0 Z" fill="url(#courtyard-tones)" role="img" aria-label="Evening rendering of the building courtyard with pool, lounge chairs and residents"/>
    </svg>
  </main>
</body>
</html>
```